International Fundraising Consultancy needs a new PowerPoint Design

We train international nonprofits on how to fundraise globally. We plan to keep our current logo design and color, as we love the color orange, but want a cleaner, fresher, less cluttered template for our PowerPoint presentations. The finished product needs to be easy to edit, and include template slides that can feature tables, graphics and images. We would like a color scheme for graphics.The layout should be lighter, clear, attractive and easy to read and understand. We also want to use the same template for webinar slides. We have attached an example of our current PowerPoint template with identifying client information removed. The green slide that looks like a clapperboard fro a film is basically just a placeholder that indicates a break for an interactive exercise.

Target Market(s)

Board members, staff members, museum executives, leadership of NGOs, top businesspeople in Europe, many with a modern sense of aesthetics in the art world

Industry/Entity Type

Cleaner

Font styles to use
Sans Serif

Colors
f78f20
f37022

Requirements
Must have
• Orange colors, keep our Vormelinck logo
• Good templates for tables, photos and graphics

```html
<!DOCTYPE html>
<html lang="en">
<head>
<meta charset="utf-8">
<title>Vormelinck &amp; Associates – Slide</title>
<link rel="stylesheet" href="https://fonts.googleapis.com/css2?family=Exo+2:wght@300;400;600&family=Roboto+Condensed:wght@400;700&display=swap">
<style>
  :root {
    --orange: #f0922b;
    --ink: #1f1f1f;
    --paper: #ffffff;
    --photo-light: #b9b6b2;
    --photo-mid: #8f8c88;
    --photo-dark: #4e4c4a;
  }
  * { margin: 0; padding: 0; box-sizing: border-box; }
  html, body {
    width: 1200px;
    height: 849px;
    overflow: hidden;
    background: var(--paper);
  }
  .slide {
    position: relative;
    width: 1200px;
    height: 849px;
    background: var(--paper);
    overflow: hidden;
  }
  .photo-panel {
    position: absolute;
    inset: 0;
    width: 1200px;
    height: 849px;
  }
  .headline {
    position: absolute;
    left: 91px;
    top: 66px;
    font-family: "Exo 2", sans-serif;
    font-weight: 300;
    font-size: 52px;
    line-height: 53px;
    color: var(--ink);
    white-space: nowrap;
  }
  .date {
    position: absolute;
    left: 93px;
    top: 302px;
    font-family: "Exo 2", sans-serif;
    font-size: 28px;
    color: var(--orange);
    letter-spacing: 0.5px;
  }
  .date .month { font-weight: 400; }
  .date .year { font-weight: 600; }
  .brand {
    position: absolute;
    left: 224px;
    top: 534px;
    display: flex;
    flex-direction: column;
  }
  .brand-name {
    font-family: "Roboto Condensed", sans-serif;
    font-weight: 400;
    font-size: 44px;
    line-height: 48px;
    color: var(--orange);
    white-space: nowrap;
  }
  .brand-tagline {
    font-family: "Roboto Condensed", sans-serif;
    font-weight: 700;
    font-size: 22px;
    line-height: 26px;
    letter-spacing: 0.4px;
    color: var(--orange);
  }
  .website {
    position: absolute;
    left: 110px;
    top: 772px;
    font-family: "Roboto Condensed", sans-serif;
    font-weight: 400;
    font-size: 25px;
    color: var(--orange);
  }
</style>
</head>
<body>
  <main class="slide">
    <svg class="photo-panel" viewBox="0 0 1200 849" role="img" aria-label="Black and white photograph of a small child eating an apple beside large metal containers">
      <defs>
        <linearGradient id="photoTone" x1="0" y1="0" x2="1" y2="1">
          <stop offset="0" stop-color="#b9b6b2"/>
          <stop offset="0.55" stop-color="#8f8c88"/>
          <stop offset="1" stop-color="#4e4c4a"/>
        </linearGradient>
      </defs>
      <path d="M560 0 C 800 150, 800 700, 560 849 L1200 849 L1200 0 Z" fill="url(#photoTone)"/>
    </svg>

    <h1 class="headline">You helped launch<br>our international<br>program quickly<br>and efficiently...</h1>

    <p class="date"><span class="month">FEB,</span> <span class="year">2015</span></p>

    <div class="brand">
      <span class="brand-name">Vormelinck &amp; Associates</span>
      <span class="brand-tagline">Fundraising Counsel</span>
    </div>

    <p class="website">www.vormelinck.com</p>
  </main>
</body>
</html>
```